Business card design needed

I need a business card design for a dog walking, dog minding and dog training business. Please refer to my website for the basic company colours and fonts I'm after. Planning on a double sided card, so all information doesn't need to be on the 'front' side.
Cheers

Industry/Entity Type

Dog Training

Contact Information for Business Card

Meadow Paws - happy hounds
Rua 0498307164
meadowpawsdemo.com.au
-walking
-holiday stays
-onsite care
-training and behavioural consultations

```html
<!DOCTYPE html>
<html lang="en">
<head>
<meta charset="utf-8">
<title>Meadow Paws – business card</title>
<link rel="stylesheet" href="https://fonts.googleapis.com/css2?family=Enriqueta:wght@400;600;700&family=PT+Sans:wght@400;700&display=swap">
<style>
  :root {
    --page: #ffffff;
    --frame: #555555;
    --card: #000000;
    --gold: #f0ae4a;
    --white: #ffffff;
    --rule: #8a8a8a;
  }
  * { margin: 0; padding: 0; box-sizing: border-box; }
  html, body { width: 1200px; height: 901px; overflow: hidden; background: var(--page); }
  .sheet {
    position: relative; width: 1200px; height: 901px;
    border: 2px solid var(--frame);
    font-family: "Enriqueta", Georgia, serif;
  }
  .card { position: absolute; left: 332px; width: 610px; height: 349px; background: var(--card); overflow: hidden; }
  .card--front { top: 123px; }
  .card--back { top: 510px; }
  .t { position: absolute; white-space: nowrap; line-height: 1; color: var(--gold); }

  .front-name { left: 0; width: 100%; top: 130px; text-align: center; font-size: 52px; }
  .front-name .accent { color: var(--white); }
  .front-tagline { left: 0; width: 100%; top: 188px; text-align: center; font-size: 26px; font-weight: 600; }

  .back-name { left: 34px; top: 66px; font-size: 44px; }
  .divider { position: absolute; left: 328px; top: 42px; width: 1px; height: 163px; background: var(--rule); }
  .holder { left: 342px; top: 50px; font-size: 30px; }
  .back-tagline { left: 342px; top: 86px; font-size: 15px; font-weight: 700; }
  .services-a { left: 342px; top: 105px; font-size: 12px; font-weight: 700; }
  .phone { left: 342px; top: 121px; font-size: 21px; font-family: "PT Sans", Verdana, sans-serif; }
  .services-b { left: 342px; top: 150px; font-size: 11.5px; font-weight: 700; }
  .services-c { left: 342px; top: 165px; font-size: 11.5px; font-weight: 700; }
  .services-d { left: 342px; top: 180px; font-size: 20px; font-family: "PT Sans", Verdana, sans-serif; }
  .website { left: 0; width: 100%; padding-left: 40px; top: 321px; text-align: center; font-size: 18px; font-weight: 700; }
</style>
</head>
<body>
  <main class="sheet">
    <section class="card card--front" aria-label="Card front">
      <div class="t front-name">Meadow <span class="accent">Paws</span></div>
      <div class="t front-tagline">happy hounds</div>
    </section>

    <section class="card card--back" aria-label="Card back">
      <div class="t back-name">Meadow Paws</div>
      <div class="divider"></div>
      <div class="t holder">Rua</div>
      <div class="t back-tagline">happy hounds</div>
      <div class="t services-a">walking -holiday stays</div>
      <div class="t phone">0498307164</div>
      <div class="t services-b">training and</div>
      <div class="t services-c">behavioural consultations</div>
      <div class="t services-d">onsite care</div>
      <div class="t website">meadowpawsdemo.com.au</div>
    </section>
  </main>
</body>
</html>
```